Off Grid consulting and outdoor products needs a website

We need a website design to help launch our new business. Its a business that plans to offer Off-grid conslting and outdoor survival products to people who are looking to relocate or vacation to properties/homes that are Off-grid. We plan to offer design plans for homes/cabins, renewable energy systems for power/heating etc, survival products for outdoor vacations/living. We also do consulting and project management for those who want to design and build from scratch their dream off-grid home or vacation property. I've included our logo design for use.
Would like the website to include 5 pages.
www.ridgepinehaven.com
The main landing page (1)
want a video loop backround with a flyover of a cabin in the woods.
https://www.clipvaultora.com/video/clip-48291736-blue-sky-melting-snow-on-green-energy
(also need a backup static image of just high-shot of cabin in woods)
logo top left, Quoted string of text in the middle, over the video. and a CTA button to 'Contact us'
picture links below that to last 3 recent blog posts.
About Us page (2)
(example) https://larkwildgear.com/pages/about-lark
Blog page (3)
blog posts associated with pictures.
Consulting 'services' page (4)
-land services and moving off-grid
-Building off grid
-Renewable energy off-grid
-Sustainable farming and all season greenhouses
Store page 'comming soon' (5)
(Example) http://timberly.crestlayouts.com/demo-1/demo.html

Target Market(s)

Outdoor enthusiasts and people who want to escape their city life

Coding

Coded - Design and coding required

Requirements
Must have
• Outdoor feel, woods, cabin, reneable energy (solar, geothermal, greenhouses, water wells)

```html
<!DOCTYPE html>
<html lang="en">
<head>
<meta charset="utf-8">
<title>Ridgepine Haven – Off Grid Consulting</title>
<link href="https://fonts.googleapis.com/css2?family=Oswald:wght@400;500;600;700&family=Poppins:wght@300;400;600;700&family=Open+Sans:wght@400;600&display=swap" rel="stylesheet">
<style>
:root{
  --orange:#c8870e;
  --brown:#3f2612;
  --brown-line:#6b4a2c;
  --submit:#6b3d17;
  --black:#0a0a0a;
  --ink:#1b1b1b;
  --text:#333;
  --white:#fff;
  --card-dark:#2b2b2b;
}
*{margin:0;padding:0;box-sizing:border-box}
html,body{width:1200px;height:3633px;overflow:hidden}
body{position:relative;background:var(--white);font-family:"Open Sans",sans-serif;color:var(--text)}
.abs{position:absolute}
.fill{position:absolute}
/* hero */
.hero-photo{left:0;top:0;width:1200px;height:540px;background:linear-gradient(180deg,#6f7a84 0%,#8c969c 20%,#5b6460 45%,#2f3a35 75%,#1f2824 100%)}
.logo{display:flex;align-items:center;gap:8px;font-family:"Oswald",sans-serif;font-weight:700;font-size:22px;color:var(--white);text-transform:uppercase;letter-spacing:.5px}
.logo-mark{width:22px;height:22px;background:currentColor;display:inline-block}
.nav{left:0;top:50px;width:1200px;height:20px;font-family:"Poppins",sans-serif;font-size:13px;color:var(--white)}
.nav a{position:absolute;color:inherit;text-decoration:none;white-space:nowrap}
.play{left:569px;top:181px;width:62px;height:62px;border-radius:50%;background:var(--white);border:3px solid #ddd}
.hero-title{left:0;top:262px;width:1200px;text-align:center;font-family:"Poppins",sans-serif;font-weight:700;font-size:25px;color:var(--white);text-transform:uppercase}
.hero-sub{left:0;top:300px;width:1200px;text-align:center;font-family:"Poppins",sans-serif;font-weight:300;font-size:21px;line-height:30px;color:var(--white);text-transform:uppercase}
.btn{left:525px;top:376px;width:150px;height:42px;border-radius:21px;background:var(--orange);color:var(--white);font-family:"Poppins",sans-serif;font-size:13px;display:flex;align-items:center;justify-content:center}
/* sections */
.ghost{left:0;width:1200px;text-align:center;font-family:"Oswald",sans-serif;font-weight:700;font-size:110px;color:transparent;-webkit-text-stroke:1px rgba(0,0,0,.12);text-transform:uppercase;line-height:1}
.ghost.light{-webkit-text-stroke:1px rgba(255,255,255,.16)}
.h2{left:0;width:1200px;text-align:center;font-family:"Oswald",sans-serif;font-weight:700;font-style:italic;font-size:52px;text-transform:uppercase;line-height:1}
.about-bg{left:0;top:540px;width:1200px;height:660px;background:linear-gradient(180deg,#fff 0%,#f3f4f4 60%,#e6e9ea 100%)}
.about-col{top:722px;width:412px;font-size:13px;line-height:25.6px;color:var(--text)}
.more{font-family:"Poppins",sans-serif;font-size:13px;color:var(--ink);display:flex;align-items:flex-end;gap:6px}
.more .sq{width:26px;height:26px;background:currentColor}
.more span{border-bottom:1px solid currentColor;padding:0 20px 2px 0}
/* services */
.card{top:1310px;width:202px;background:var(--white)}
.card .img{height:226px}
.card .label{height:72px;display:flex;align-items:center;justify-content:center;text-align:center;font-family:"Oswald",sans-serif;font-size:15px;line-height:20px;color:var(--ink);text-transform:uppercase;padding:0 10px}
.card.active{background:var(--card-dark);height:480px}
.card.active .label{color:var(--white);height:60px;align-items:flex-end}
.card-text{font-size:13px;line-height:20px;color:#ddd;text-align:center;padding:8px 18px 0}
.card-mark{justify-content:center;margin-top:30px;font-size:20px}
/* blog */
.post-big{left:161px;top:2125px;width:431px;height:383px;background:linear-gradient(180deg,#8ea5a6 0%,#6d8482 40%,#4c5a3e 70%,#3b4a2b 100%)}
.post-big .meta{position:absolute;left:36px;top:268px;width:370px;color:var(--white)}
.date{font-size:11px;color:var(--white)}
.ptitle{font-family:"Oswald",sans-serif;font-size:15px;line-height:20px;margin-top:12px;color:var(--white)}
.pexc{font-size:12.5px;line-height:20px;margin-top:8px;color:#e8e2da}
.post-small{left:617px;width:422px;height:180px;border:1px solid var(--brown-line)}
.post-small .img{position:absolute;left:6px;top:6px;width:166px;height:165px}
.post-small .meta{position:absolute;left:192px;top:20px;width:215px}
/* offers */
.offer-title{left:0;top:2808px;width:1200px;text-align:center;font-family:"Oswald",sans-serif;font-weight:600;font-size:46px;color:var(--ink);text-transform:uppercase}
.offer-sub{left:0;top:2868px;width:1200px;text-align:center;font-family:"Oswald",sans-serif;font-size:20px;line-height:29px;color:var(--ink);text-transform:uppercase}
/* footer */
.footer-bg{left:0;top:3123px;width:1200px;height:510px;background:linear-gradient(180deg,#3c4a55 0%,#2e3b3c 45%,#22302a 100%)}
.fh{font-family:"Oswald",sans-serif;font-weight:600;font-style:italic;font-size:26px;color:var(--white);text-transform:uppercase}
.field{height:36px;border:1px solid rgba(255,255,255,.45);background:rgba(255,255,255,.08);color:#e6e6e6;font-size:11.5px;display:flex;align-items:center;padding-left:8px;gap:6px}
.field.msg{align-items:flex-start;padding-top:10px}
.field svg{flex:none}
.submit{left:161px;top:3425px;width:160px;height:36px;background:var(--submit);color:var(--white);font-family:"Oswald",sans-serif;font-size:19px;display:flex;align-items:center;justify-content:center}
.contact-row{left:798px;display:flex;gap:10px;color:var(--white);font-family:"Poppins",sans-serif;font-size:15px;line-height:22px}
.copy{left:162px;top:3572px;font-size:12.5px;line-height:20px;color:#e8e8e8}
.social{top:3580px;width:28px;height:28px;border-radius:50%;background:var(--orange)}
</style>
</head>
<body>

<!-- Hero -->
<div class="fill hero-photo" role="img" aria-label="Aerial video still of a cabin in snowy pine forest among mountains"></div>
<div class="abs logo" style="left:162px;top:44px;font-size:24px"><i class="logo-mark"></i>Ridgepine Haven</div>
<nav class="abs nav">
  <a style="left:469px">Home</a>
  <a style="left:583px">About Us</a>
  <a style="left:720px">Services</a>
  <a style="left:851px">Blogs</a>
  <a style="left:963px">Contact Us</a>
</nav>
<div class="abs play"></div>
<svg class="abs" style="left:589px;top:199px" width="26" height="26" viewBox="0 0 26 26"><path d="M4 2 L22 13 L4 24Z" fill="#b8531b"/></svg>
<h1 class="abs hero-title">We offer off grid consulting &amp; outdoor survival products</h1>
<p class="abs hero-sub">To people who are looking to relocate or vacation to homes<br>that are off grid / away from city</p>
<a class="abs btn">Contact Us</a>

<svg class="abs" style="left:0;top:330px" width="1200" height="260" viewBox="0 0 1200 260">
  <path d="M0 15 C220 150 420 210 600 205 C820 200 1020 140 1200 95 L1200 260 L0 260Z" fill="#c8870e"/>
  <path d="M0 30 C220 160 420 200 600 200 C820 198 1020 150 1200 115 L1200 260 L0 260Z" fill="#8a4a1a"/>
  <path d="M0 45 C220 170 420 205 600 207 C820 207 1020 160 1200 125 L1200 260 L0 260Z" fill="#fff"/>
</svg>

<!-- About -->
<div class="fill about-bg" role="img" aria-label="Faded photo of a snowy cabin beside a frozen lake"></div>
<div class="abs ghost" style="top:570px">About</div>
<h2 class="abs h2" style="top:632px;color:var(--black)">About Ridgepine</h2>
<div class="abs" style="left:0;top:684px;width:1200px;text-align:center;font-family:'Oswald',sans-serif;font-style:italic;font-size:15px;color:var(--ink)">HAVEN</div>
<p class="abs about-col" style="left:162px">Lorem ipsum dolor sit amet, consectetuer adipiscing elit, sed diam nonummy nibh euismod tincidunt ut laoreet dolore magna aliquam erat volutpat. Ut wisi enim ad minim veniam, quis nostrud exerci tation ullamcorper suscipit lobortis nisl ut aliquip ex ea commodo consequat. Duis autem vel eum iriure dolor in hendrerit in vulputate velit esse molestie</p>
<p class="abs about-col" style="left:624px">Lorem ipsum dolor sit amet, consectetuer adipiscing elit, sed diam nonummy nibh euismod tincidunt ut laoreet dolore magna aliquam erat volutpat. Ut wisi enim ad minim veniam, quis nostrud exerci tation ullamcorper suscipit lobortis nisl ut aliquip ex ea commodo consequat. Duis autem vel eum iriure dolor in hendrerit in vulputate velit esse molestie</p>
<a class="abs more" style="left:540px;top:915px"><i class="sq"></i><span>READ MORE</span></a>

<!-- Dark / brown bands -->
<svg class="abs" style="left:0;top:960px" width="1200" height="1880" viewBox="0 0 1200 1880">
  <path d="M0 8 L1200 240 L1200 1880 L0 1880Z" fill="#0a0a0a"/>
  <path d="M1200 773 L1200 1840 L0 1610 L0 1080Z" fill="#3f2612"/>
  <path d="M0 1610 L1200 1840 L1200 1880 L0 1880Z" fill="#fff"/>
</svg>

<!-- Services -->
<div class="abs ghost light" style="top:1150px">Services</div>
<h2 class="abs h2" style="top:1215px;color:var(--white)">Our Services</h2>
<div class="abs card" style="left:161px">
  <div class="img" role="img" aria-label="A-frame tent cabin on a wooden deck in green forest" style="background:linear-gradient(180deg,#6f8f4a,#8f7a5a 60%,#6b5238)"></div>
  <div class="label">Land services and<br>moving off-grid</div>
</div>
<div class="abs card active" style="left:386px">
  <div class="img" role="img" aria-label="Yellow wooden house on rocky shore under misty sky" style="background:linear-gradient(180deg,#9fb0b8,#c7a13a 55%,#3a3a3a)"></div>
  <div class="label">Building off grid</div>
  <p class="card-text">Lorem ipsum dolor sit amet, consectetuer adipiscing elit, sed diam nonummy nibh euismod</p>
  <div class="logo card-mark"><i class="logo-mark"></i>Ridgepine Haven</div>
</div>
<div class="abs card" style="left:611px">
  <div class="img" role="img" aria-label="Lit timber house at dusk in snowy woods" style="background:linear-gradient(180deg,#3d4556,#5b4a3c 55%,#c27a33 75%,#5a5a66)"></div>
  <div class="label">Renewable energy off-grid</div>
</div>
<div class="abs card" style="left:836px">
  <div class="img" role="img" aria-label="Dark turf-roof house on green hillside" style="background:linear-gradient(180deg,#7fa05a,#3d4a3a 55%,#5e8a3c)"></div>
  <div class="label">Sustainable farming and<br>all season greenhouses</div>
</div>

<!-- Blog -->
<div class="abs ghost light" style="top:1980px">Blog</div>
<h2 class="abs h2" style="top:2043px;color:var(--white)">Latest Blog Posts</h2>
<div class="abs post-big" role="img" aria-label="Wooden red-roof cabin on a lawn beside pine trees">
  <div class="meta">
    <div class="date">14 April, 2022</div>
    <div class="ptitle">Lorem ipsum dolor sit amet, Consectetuer Adipiscing elitsed</div>
    <div class="pexc">Wisi enim ad minim veniam, quis nostrud exerci tation ullamcorper suscipit lobortis nisl ut aliquip exea</div>
  </div>
</div>
<div class="abs post-small" style="top:2124px">
  <div class="img" role="img" aria-label="Log cabin in snowy forest" style="background:linear-gradient(180deg,#c9cfd4,#6b4330 55%,#e9ecee)"></div>
  <div class="meta">
    <div class="date">14 April, 2022</div>
    <div class="ptitle">Lorem ipsum dolor sit amet, Conse ctetuer Adipiscing elitsed</div>
    <div class="pexc">Wisi enim ad minim veniam, quis nostrud exerci tation ullamc orper suscipit lobortis nisl.</div>
  </div>
</div>
<div class="abs post-small" style="top:2327px">
  <div class="img" role="img" aria-label="Log cabin among pines with rocky ground and mountains" style="background:linear-gradient(180deg,#8fa3b0,#3e4a3c 40%,#7a4a32 65%,#8a8e90)"></div>
  <div class="meta">
    <div class="date">14 April, 2022</div>
    <div class="ptitle">Lorem ipsum dolor sit amet, Conse ctetuer Adipiscing elitsed</div>
    <div class="pexc">Wisi enim ad minim veniam, quis nostrud exerci tation ullamc orper suscipit lobortis nisl.</div>
  </div>
</div>
<a class="abs more" style="left:524px;top:2548px;color:var(--white)"><i class="sq"></i><span>VIEW ALL POSTS</span></a>

<!-- Design plans -->
<h2 class="abs offer-title">We also offer design plans for</h2>
<p class="abs offer-sub">Homes/cabins, renewable energy systems for power/heating etc, survival<br>products for outdoor vacations/living</p>
<a class="abs more" style="left:526px;top:2945px"><i class="sq"></i><span>VIEW ALL POSTS</span></a>

<!-- Footer -->
<div class="fill footer-bg" role="img" aria-label="Mountain valley with a turf-roof cabin under clouds"></div>
<h3 class="abs fh" style="left:161px;top:3180px">Quick Inquiry</h3>
<div class="abs field" style="left:161px;top:3235px;width:244px"><svg width="11" height="11" viewBox="0 0 12 12"><circle cx="6" cy="3.5" r="3" fill="#ddd"/><path d="M0 12c0-4 12-4 12 0z" fill="#ddd"/></svg>First Name*</div>
<div class="abs field" style="left:419px;top:3235px;width:243px"><svg width="11" height="11" viewBox="0 0 12 12"><circle cx="6" cy="3.5" r="3" fill="#ddd"/><path d="M0 12c0-4 12-4 12 0z" fill="#ddd"/></svg>Last Name*</div>
<div class="abs field" style="left:161px;top:3285px;width:244px"><svg width="11" height="11" viewBox="0 0 12 12"><path d="M2 1l3 3-1.5 1.5c1 2 2 3 3 3L8 7l3 3-2 2C4 11 1 8 0 3z" fill="#ddd"/></svg>Phone*</div>
<div class="abs field" style="left:419px;top:3285px;width:243px"><svg width="11" height="11" viewBox="0 0 12 12"><path d="M0 6L12 0 9 12 6 8z" fill="#ddd"/></svg>Email*</div>
<div class="abs field msg" style="left:161px;top:3335px;width:501px;height:75px"><svg width="11" height="11" viewBox="0 0 12 12"><rect x="0.5" y="2" width="9" height="9.5" fill="none" stroke="#ddd"/><path d="M5 7l6-6" stroke="#ddd" stroke-width="1.5"/></svg>Message*</div>
<div class="abs submit">SUBMIT NOW</div>

<h3 class="abs fh" style="left:798px;top:3180px">Get In Touch</h3>
<p class="abs" style="left:798px;top:3240px;width:250px;font-size:12.5px;line-height:17px;color:#e6e6e6">Lorem ipsum dolor sit amet consectet adipiscing elit, sed diam nonummy.</p>
<div class="abs contact-row" style="top:3292px">
  <svg width="32" height="32" viewBox="0 0 32 32" fill="none" stroke="#fff" stroke-width="1.5"><circle cx="14" cy="18" r="11"/><path d="M3 18h22M14 7c-5 6-5 16 0 22M14 7c5 6 5 16 0 22"/><path d="M25 2a5 5 0 0 1 5 5c0 4-5 9-5 9s-5-5-5-9a5 5 0 0 1 5-5z" fill="#2e3b3c"/></svg>
  <div>123, Building Name, Street<br>City, State XY 123456</div>
</div>
<div class="abs contact-row" style="top:3360px">
  <svg width="32" height="32" viewBox="0 0 32 32" fill="none" stroke="#fff" stroke-width="1.5"><path d="M7 3l6 6-3 3c2 4 6 8 10 10l3-3 6 6-4 4C14 27 5 18 3 7z"/><path d="M19 3a10 10 0 0 1 10 10M19 8a5 5 0 0 1 5 5"/></svg>
  <div>PHONE<br>123 456 7890</div>
</div>
<div class="abs contact-row" style="top:3428px">
  <svg width="32" height="32" viewBox="0 0 32 32" fill="none" stroke="#fff" stroke-width="1.5"><rect x="2" y="10" width="28" height="20"/><path d="M2 10l14 11 14-11M7 14V3h18v11"/><path d="M11 8h10M11 12h10"/></svg>
  <div>EMAIL<br>info@ridgepinehaven.com</div>
</div>

<div class="abs" style="left:161px;top:3555px;width:878px;height:1px;background:rgba(255,255,255,.3)"></div>
<div class="abs logo" style="left:0;top:3540px;width:1200px;justify-content:center;font-size:24px"><i class="logo-mark"></i>Ridgepine Haven</div>
<p class="abs copy">Copyright © 2022 Company Name.<br>All Rights Reserved.</p>
<div class="abs social" style="left:861px"></div>
<div class="abs social" style="left:898px"></div>
<div class="abs social" style="left:935px"></div>
<div class="abs social" style="left:972px"></div>
<div class="abs social" style="left:1009px"></div>

</body>
</html>
```